Borealis Film and Design
Your Moments on Reels
Borealis Film and Design -
Creative Brief
Professional
Peter Vandrell
2187 Kettering Ln. North Pole, Alaska 99612
Peter@borealisfilmanddesign.example
borealisfilmanddesign.example

```html
<!DOCTYPE html>
<html lang="en">
<head>
<meta charset="utf-8">
<title>Borealis Film and Design – Business Card</title>
<link rel="stylesheet" href="https://fonts.googleapis.com/css2?family=Arimo:wght@400;700&display=swap">
<style>
  :root {
    --backdrop: #e7e7ea;
    --card-white: #ffffff;
    --brand-navy: #1c1f5e;
    --brand-blue: #2f3fa6;
    --band-light: #4a5cc4;
    --band-deep: #1e2a86;
    --swoosh: #111111;
    --text-light: #ffffff;
    --text-soft: #dfe4ff;
  }
  html, body {
    margin: 0;
    width: 1200px;
    height: 780px;
    overflow: hidden;
    background: var(--backdrop);
    font-family: "Arimo", Arial, sans-serif;
  }
  .business-card {
    position: absolute;
    left: 40px;
    top: 30px;
    width: 1120px;
    height: 720px;
    border-radius: 40px;
    overflow: hidden;
    background: var(--card-white);
    box-shadow: 0 10px 30px rgba(0,0,0,0.18);
  }
  .card-shapes {
    position: absolute;
    inset: 0;
  }
  .brand-lockup {
    position: absolute;
    top: 150px;
    left: 0;
    right: 0;
    display: flex;
    align-items: center;
    justify-content: center;
    gap: 24px;
  }
  .brand-dot {
    width: 78px;
    height: 78px;
    border-radius: 50%;
    background: var(--brand-blue);
  }
  .brand-name {
    font-size: 58px;
    font-weight: 700;
    color: var(--brand-navy);
    letter-spacing: 1px;
    text-transform: uppercase;
  }
  .holder {
    position: absolute;
    right: 590px;
    top: 455px;
    text-align: right;
    color: var(--text-light);
  }
  .holder-name {
    font-size: 36px;
    font-weight: 700;
    margin: 0 0 40px;
  }
  .holder-address {
    font-size: 27px;
    line-height: 1.3;
    color: var(--text-soft);
    margin: 0;
  }
  .divider {
    position: absolute;
    left: 555px;
    top: 420px;
    width: 3px;
    height: 250px;
    background: var(--text-light);
  }
  .contact-list {
    position: absolute;
    left: 580px;
    top: 420px;
    margin: 0;
    padding: 0;
    list-style: none;
    color: var(--text-light);
    font-size: 26px;
  }
  .contact-list li {
    display: flex;
    align-items: center;
    gap: 14px;
    height: 46px;
  }
  .contact-icon {
    width: 28px;
    height: 28px;
    flex: none;
  }
  .contact-list .license {
    padding-left: 42px;
  }
</style>
</head>
<body>
  <div class="business-card">
    <svg class="card-shapes" viewBox="0 0 1120 720" preserveAspectRatio="none" aria-hidden="true">
      <defs>
        <linearGradient id="bandFill" x1="0" y1="0" x2="0" y2="1">
          <stop offset="0" stop-color="var(--band-light)"/>
          <stop offset="1" stop-color="var(--band-deep)"/>
        </linearGradient>
      </defs>
      <path d="M0 360 C 250 410, 520 380, 760 330 C 900 300, 1020 285, 1120 290 L1120 720 L0 720 Z" fill="url(#bandFill)"/>
      <path d="M0 352 C 250 392, 520 362, 760 310 C 900 280, 1020 268, 1120 272 L1120 292 C 1020 290, 900 304, 760 334 C 520 384, 250 414, 0 362 Z" fill="var(--swoosh)"/>
    </svg>

    <div class="brand-lockup">
      <div class="brand-dot"></div>
      <div class="brand-name">Borealis Film and Design</div>
    </div>

    <div class="holder">
      <p class="holder-name">Peter Vandrell</p>
      <p class="holder-address">2187 Kettering Ln.<br>North Pole, Alaska 99612</p>
    </div>

    <div class="divider"></div>

    <ul class="contact-list">
      <li>
        <svg class="contact-icon" viewBox="0 0 24 24" aria-hidden="true"><rect x="7" y="2" width="10" height="20" rx="2" fill="none" stroke="#fff" stroke-width="2"/><rect x="9" y="5" width="6" height="9" fill="#fff"/></svg>
        1-907-555-0182
      </li>
      <li>
        <svg class="contact-icon" viewBox="0 0 24 24" aria-hidden="true"><circle cx="12" cy="12" r="4" fill="none" stroke="#fff" stroke-width="2.4"/><path d="M16 9 V14 a3 3 0 0 0 6 0 V12 a10 10 0 1 0 -4 8" fill="none" stroke="#fff" stroke-width="2.4"/></svg>
        Peter@borealisfilmanddesign.example
      </li>
      <li>
        <svg class="contact-icon" viewBox="0 0 24 24" aria-hidden="true"><circle cx="12" cy="12" r="10" fill="none" stroke="#fff" stroke-width="2"/><ellipse cx="12" cy="12" rx="4" ry="10" fill="none" stroke="#fff" stroke-width="1.6"/><path d="M2 12 H22 M4 7 H20 M4 17 H20" stroke="#fff" stroke-width="1.4"/></svg>
        borealisfilmanddesign.example
      </li>
      <li class="license">License No : 480263</li>
    </ul>
  </div>
</body>
</html>
```